Website for residential builder repair in Australia

I currently have my website setup using Hostinger as hosting and started playing around with Wordpress.
I would like this to be able to be imported into Wordpress after built so I can add blog posts and edit site if needed.

I would like a website built that is simple and clear.

the main colours id like for the site are black and white and maybe grey.

I would like a simple welcome page, an about us page, a project page, and a blog page where I can write small articles.

will need to display licence number on website lic. 374026K

Target Market(s)

young to middle age families and couples looking to build a sustainable and high performance house.

Contact Information for Business Card

Quarry Lane Building
Lic. 374026K (to be printed small)
email; miles@quarrylanebuilding.com.au
phone : 0428163950

Miles Venner - Director

Number of Pages Required

4 page

Font styles to use
Sans Serif
Other font styles liked:
• match logo

Colors

Designer to choose only greyscale colors for use in the design.

Requirements
Must have
• outline of works

Certified Passive House Tradesperson
New Builds
Renovations
Architectural homes
Nice to have
• thinking dark grey background or black

would like to see the logo embossed to look slightly 3d

back of card to be white or light grey so It can be written on.

letterhead to contain licence number swell

```html
<!DOCTYPE html>
<html lang="en">
<head>
<meta charset="utf-8">
<title>Quarry Lane Building – Letterhead</title>
<link rel="stylesheet" href="https://fonts.googleapis.com/css2?family=Jost:wght@300;400&display=swap">
<style>
  :root {
    --paper: #ffffff;
    --ink: #3a3a3a;
    --ink-soft: #4a4a4a;
    --accent: #8c8c8c;
    --backdrop-mark: #f5f5f5;
  }
  html, body {
    margin: 0;
    padding: 0;
    overflow: hidden;
    background: var(--paper);
  }
  .letterhead {
    position: relative;
    width: 848px;
    height: 1200px;
    background: var(--paper);
    font-family: "Jost", sans-serif;
    color: var(--ink);
    overflow: hidden;
  }
  .edge-bar {
    position: absolute;
    left: 0;
    top: 34px;
    width: 10px;
    height: 197px;
    background: var(--accent);
  }
  .backdrop-mark {
    position: absolute;
    left: 104px;
    top: 262px;
    width: 640px;
    height: 640px;
    background: var(--backdrop-mark);
  }
  .brand {
    position: absolute;
    left: 97px;
    top: 96px;
    width: 220px;
    text-align: center;
  }
  .brand-name {
    margin: 0;
    font-size: 17px;
    font-weight: 400;
    letter-spacing: 5px;
    line-height: 22px;
    color: var(--ink);
    text-transform: uppercase;
  }
  .brand-licence {
    margin: 18px 0 0;
    font-size: 12.5px;
    font-weight: 300;
    color: var(--ink);
  }
  .contact {
    position: absolute;
    right: 104px;
    top: 93px;
    margin: 0;
    text-align: right;
    font-style: normal;
    font-size: 12px;
    font-weight: 300;
    line-height: 20.5px;
    color: var(--ink);
  }
  .header-rule {
    position: absolute;
    left: 106px;
    top: 232px;
    width: 636px;
    height: 1px;
    background: var(--accent);
  }
  .letter-body {
    position: absolute;
    left: 104px;
    top: 346px;
    width: 642px;
    font-size: 16.5px;
    font-weight: 300;
    letter-spacing: 0.35px;
    line-height: 21.3px;
    color: var(--ink-soft);
  }
  .letter-body p {
    margin: 0 0 21px;
    text-align: justify;
  }
  .letter-body .salutation {
    margin-bottom: 19px;
  }
  .letter-body .sign-off {
    text-align: left;
  }
</style>
</head>
<body>
  <main class="letterhead">
    <div class="edge-bar"></div>
    <div class="backdrop-mark"></div>

    <header>
      <div class="brand">
        <p class="brand-name">Quarry Lane<br>Building</p>
        <p class="brand-licence">Lic. 374026K</p>
      </div>
      <address class="contact">
        Street Name<br>
        Postal Code / City<br>
        Email : miles@quarrylanebuilding.com.au<br>
        Phone : 0428163950
      </address>
      <div class="header-rule"></div>
    </header>

    <section class="letter-body">
      <p class="salutation">Dear Ms/Mr (Name),</p>
      <p>Lorem ipsum dolor sit amet, consectetuer adipiscing elit, sed diam nonummy nibh euismod tincidunt ut laoreet dolore magna aliquam erat volutpat. Ut wisi enim ad minim veniam, quis nostrud exerci tation ullamcorper suscipit lobortis nisl ut aliquip ex ea commodo consequat. Duis autem vel eum iriure dolor in hendrerit in vulputate velit esse molestie consequat, vel illum dolore eu feugiat nulla facilisis at vero eros et accumsan et iusto odio dignissim qui blandit praesent luptatum zzril</p>
      <p>Lorem ipsum dolor sit amet, cons ectetuer adipiscing elit, sed diam nonummy nibh euismod tincidunt ut laoreet dolore magna aliquam erat volutpat. Ut wisi enim ad minim veniam, quis nostrud exerci tation ullamcorper suscipit lobortis nisl ut aliquip ex ea commodo consequat.</p>
      <p>Lorem ipsum dolor sit amet, consectetuer adipiscing elit, sed diam nonummy nibh euismod tincidunt ut laoreet dolore magna aliquam erat volutpat. Ut wisi enim ad minim veniam, quis nostrud exerci tation ullamcorper suscipit lobortis nisl ut aliquip ex ea commodo consequat. Duis autem vel eum iriure dolor in hendrerit in vulputate velit esse molestie consequat, vel illum dolore eu feugiat nulla facilisis at vero eros et accum</p>
      <p>Lorem ipsum dolor sit amet, consectetuer adipiscing elit, sed diam nonummy nibh euismod tincidunt ut laoreet dolore magna aliquam erat volutpat.</p>
      <p class="sign-off">Best Regards,<br>Your Name</p>
    </section>
  </main>
</body>
</html>
```